依頼詳細
まずは、顔となる表面のデザインをお願いします。
(本件採用後、裏面詳細データの作成を依頼いたします。)
サイズ:250巾×200ピッチ(縦横は問いません)
材質:CP/OPのナイロンです。(デザインによりマット調のナイロンも使用可能とします)

【ターゲットにしたい顧客】
「女性」なら、夜ふかしスイーツ的な逸品
「男性」なら、甘いもの好きの小腹サポート
「子供」なら、ゼリーに代わるおやつ
「お土産」なら、京都とか、京都伏見とかの地元感。
「外国人観光客」なら、京都伏見を連想させるお土産。
「観光客」なら、松葉駅でのお土産。
「海外輸出」現在、日本食など人気があるので、外国人にも受け入れられるデザイン

主に一般スーパーやドラックストアーの販売店に販売してもらいますが、高級志向店やお土産物屋さんにも流通させるつもりです。
京都から離れた、名古屋・東京・仙台 などを中心とした販売を考えています。
京都や京都伏見を目立つようにデザインを立ててください。

【商品形状】
添付資料で、調理済み写真を添付します。
写真を利用したパッケージデザインをお願いします。

【商品特徴】
食感にこだわり、モッちもちな食感に仕上げたこんにゃくゼリーです。
わらび餅を一切使用しておらず、わらび餅風にこんにゃくゼリーです。
3種類とも全て間食して頂いて100kcal未満です。(添付物を含む)
記載項目
【商品ネーミング】
(現在『わらび餅風味こんにゃく 白糖味・黒蜜味・抹茶味』)
・京都伏見のわらび餅風味こんにゃく
・京都伏見のわらび餅風こんにゃく
・京都・白瀬明神のわらび餅風こんにゃく
・京都伏見のわらび餅風蒟蒻
・京都伏見のまるでわらび餅
・京都伏見のモッちり餅
・京都・白瀬明神のわらび餅みたいな蒟蒻

【副題として】
『京都伏見・白瀬明神・大正7年創業・創業100余年・老舗浜岡自慢の逸品』の語句をデザインに含めてください
希望イメージ
• +5 0 +5
• シンプル
複雑
• 単色
カラフル
• 暗い
明るい
• 日常
高級
• 遊び心
厳粛
• 未来的
伝統的
• 女性的
男性的
希望する色
納品ファイル
• 高解像度JPG (.jpg)
• イラストレーター形式 (.ai)
• フォトショップ形式 (.psd)
• PNG形式 (.png)
補足説明
現行品のデザインを掲載いたします。
調理例の写真データをご使用下さい。

依頼公開後の追記内容
※裏面データの作成について
現行品の裏面データを添付ファイルで掲示させていただきます。
ご参考の程、宜しくお願い致します。
なお、内容に関しましては、食品表示法改正に伴い変更をお願いする予定です。
素敵なデザインをありがとうございます。
もう少し、ご提案を頂きたいので、締め切り日を延期させて頂きました。
■ 選んだ理由

全ての素晴らしいデザインの中より選定を行うのにかなりの時間が掛かりましたが、とくに今回のデザインの中で、『雅ふわ乃』のネーミング付きデザインがとても気に入りました。

日配商品のルートで流通させるのが惜しいほどのデザインです。京都のお土産としても売り込んでいこうと思っております。

■ 提案者全員のお礼・コメント

今回も多くのご応募を頂き、誠に有難うございます。

今回の依頼では、応募期間を規定値よりも更に延ばさせてもらいましたが、その分、応募総数が大いに増え、選定に時間が掛かってしまい申し訳ございませんでした。
それと、私の思いが大きすぎて、長文での依頼内容となりましたが、それを理解して頂き素敵なご提案をして下さる皆様へは本当に感謝の気持ちでいっぱいです。

また次回も素敵なご提案を宜しくお願い致します。

本当にありがとうございました

```html
<!DOCTYPE html>
<html lang="ja">
<head>
<meta charset="utf-8">
<title>京都白瀬のくずもち風 はんなり蒟蒻 黒蜜味</title>
<link href="https://fonts.googleapis.com/css2?family=Shippori+Mincho+B1:wght@600;800&family=Zen+Maru+Gothic:wght@700&display=swap" rel="stylesheet">
<style>
:root{
  --paper:#ffffff;
  --plum:#b81f5c;
  --plum-deep:#8e1446;
  --plum-light:#d9588a;
  --gold:#e8a23a;
  --gold-light:#f7d46b;
  --ink:#2b2a36;
  --cream:#fbf4ea;
  --plate:#6f93c4;
  --syrup:#4a2a1c;
}
*{margin:0;padding:0;box-sizing:border-box}
html,body{width:897px;height:1200px;overflow:hidden;background:var(--paper)}
body{position:relative;font-family:"Shippori Mincho B1",serif}
.pack{position:absolute;left:66px;top:24px;width:771px;height:1166px;background:var(--plum);overflow:hidden}
.pack-edge{position:absolute;left:0;width:771px;height:14px}
.pack-edge.top{top:0}
.pack-edge.bottom{bottom:0}
.top-band{position:absolute;left:0;top:0;width:771px;height:70px;background:linear-gradient(90deg,var(--plum-light),var(--plum))}
.pattern-left{position:absolute;left:-40px;top:260px;width:200px;height:300px;border-radius:0 150px 150px 0;background:linear-gradient(160deg,var(--gold-light),var(--gold))}
.pattern-right{position:absolute;right:-60px;top:20px;width:220px;height:220px;border-radius:50%;background:linear-gradient(200deg,var(--gold-light),var(--gold));opacity:.85}
.pattern-bottom{position:absolute;left:0;bottom:0;width:771px;height:170px;background:linear-gradient(180deg,var(--plum),var(--plum-deep))}
.emblem{position:absolute;left:139px;top:56px;width:500px;height:500px;border-radius:50%;background:var(--ink);border:6px solid var(--cream)}
.title{position:absolute;left:139px;width:500px;text-align:center;color:var(--paper);font-weight:800;line-height:1}
.title.place{top:82px;font-size:48px}
.title.style{top:142px;font-size:58px}
.title.texture{top:212px;font-size:82px}
.title.name{top:300px;left:270px;width:330px;font-size:150px;letter-spacing:-4px}
.ruby{position:absolute;left:335px;top:462px;width:200px;text-align:center;color:var(--paper);font-size:20px;letter-spacing:4px}
.heritage{position:absolute;top:300px;writing-mode:vertical-rl;color:var(--paper);font-weight:600;font-size:25px;letter-spacing:2px}
.heritage.founded{left:232px}
.heritage.shop{left:198px}
.knot{position:absolute;left:324px;top:490px;width:130px;height:120px;border-radius:50%;background:radial-gradient(circle,var(--plum-light),var(--plum) 70%);border:5px solid var(--cream)}
.blossom{position:absolute;left:540px;top:60px;width:40px;height:40px;border-radius:50%;background:var(--plum-light)}
.photo{position:absolute;left:170px;top:700px;width:440px;height:300px;border-radius:24px;background:linear-gradient(160deg,var(--plate),#3f6aa4 45%,var(--syrup) 100%)}
.flavor{position:absolute;left:550px;top:456px;width:136px;height:210px;background:var(--paper);border:4px solid var(--ink);text-align:center;color:var(--ink)}
.flavor-name{display:block;font-weight:800;font-size:60px;line-height:1;margin-top:22px;writing-mode:vertical-rl;margin-left:auto;margin-right:auto;height:124px}
.flavor-note{display:block;font-weight:800;font-size:34px;line-height:1;margin-top:6px}
.extra{position:absolute;left:594px;top:666px;width:180px;height:88px;background:var(--gold-light);clip-path:polygon(12% 0,100% 0,100% 100%,12% 100%,0 50%);display:flex;align-items:center;justify-content:center;padding-left:18px;color:var(--plum);font-family:"Zen Maru Gothic",sans-serif;font-size:30px;line-height:1.05;text-align:center}
.tagline{position:absolute;left:46px;top:694px;width:250px;padding:8px 10px;background:var(--cream);border:3px solid var(--plum-deep);color:var(--ink);font-family:"Zen Maru Gothic",sans-serif;font-size:22px;line-height:1.3;text-align:center}
.tagline em{font-style:normal;color:var(--plum)}
.calorie{position:absolute;left:24px;top:1030px;width:120px;text-align:center;color:var(--gold-light);font-family:"Zen Maru Gothic",sans-serif;line-height:1.1}
.calorie .unit{display:block;font-size:20px}
.calorie .value{display:block;font-size:34px}
.calorie .cap{display:block;font-size:22px}
</style>
</head>
<body>
<main class="pack">
  <div class="top-band"></div>
  <div class="pattern-right" role="img" aria-label="金色の波文様"></div>
  <div class="pattern-left" role="img" aria-label="金色の波文様"></div>
  <div class="pattern-bottom"></div>

  <svg class="pack-edge top" viewBox="0 0 771 14" preserveAspectRatio="none" aria-hidden="true">
    <path d="M0 0 H771 V4 L760 14 L749 4 L738 14 L727 4 L716 14 L705 4 L694 14 L683 4 L672 14 L661 4 L650 14 L639 4 L628 14 L617 4 L606 14 L595 4 L584 14 L573 4 L562 14 L551 4 L540 14 L529 4 L518 14 L507 4 L496 14 L485 4 L474 14 L463 4 L452 14 L441 4 L430 14 L419 4 L408 14 L397 4 L386 14 L375 4 L364 14 L353 4 L342 14 L331 4 L320 14 L309 4 L298 14 L287 4 L276 14 L265 4 L254 14 L243 4 L232 14 L221 4 L210 14 L199 4 L188 14 L177 4 L166 14 L155 4 L144 14 L133 4 L122 14 L111 4 L100 14 L89 4 L78 14 L67 4 L56 14 L45 4 L34 14 L23 4 L12 14 L0 4 Z" fill="#ffffff"/>
  </svg>

  <div class="emblem"></div>
  <div class="blossom" role="img" aria-label="桜の飾り"></div>
  <p class="title place">京都白瀬の</p>
  <p class="title style">くずもち風</p>
  <h1 class="title texture">はんなり</h1>
  <p class="title name">蒟蒻</p>
  <p class="ruby">こんにゃく</p>
  <p class="heritage founded">大正七年創業</p>
  <p class="heritage shop">老舗浜岡自慢の逸品</p>
  <div class="knot" role="img" aria-label="水引の結び飾り"></div>

  <div class="photo" role="img" aria-label="商品写真：器に盛った黒蜜がけのこんにゃく"></div>

  <div class="flavor">
    <span class="flavor-name">黒蜜</span>
    <span class="flavor-note">味</span>
  </div>
  <div class="extra">きな粉<br>付き</div>

  <p class="tagline">モッちもち食感の<br><em>こんにゃくゼリー</em></p>

  <p class="calorie"><span class="unit">1袋あたり</span><span class="value">100kcal</span><span class="cap">未満</span></p>

  <svg class="pack-edge bottom" viewBox="0 0 771 14" preserveAspectRatio="none" aria-hidden="true">
    <path d="M0 14 H771 V10 L760 0 L749 10 L738 0 L727 10 L716 0 L705 10 L694 0 L683 10 L672 0 L661 10 L650 0 L639 10 L628 0 L617 10 L606 0 L595 10 L584 0 L573 10 L562 0 L551 10 L540 0 L529 10 L518 0 L507 10 L496 0 L485 10 L474 0 L463 10 L452 0 L441 10 L430 0 L419 10 L408 0 L397 10 L386 0 L375 10 L364 0 L353 10 L342 0 L331 10 L320 0 L309 10 L298 0 L287 10 L276 0 L265 10 L254 0 L243 10 L232 0 L221 10 L210 0 L199 10 L188 0 L177 10 L166 0 L155 10 L144 0 L133 10 L122 0 L111 10 L100 0 L89 10 L78 0 L67 10 L56 0 L45 10 L34 0 L23 10 L12 0 L0 10 Z" fill="#ffffff"/>
  </svg>
</main>
</body>
</html>
```